BOLD & MINIMALIST DESIGN NEEDED

We want a very bold but minimalistic business card design that is impactful and utilizes both sides of the business card. Our current logo is included for your use.

We want bold fonts and good use of negative space. We don't want the logo to overpower the design.

Target Market(s)

Professionals who are building new commercial buildings.

Industry/Entity Type

Construction

Contact Information for Business Card

Name, Title, email, office phone, cell phone, website

Font styles to use
Serif
Sans Serif

Requirements
Must have
• Bold design!

```html
<!DOCTYPE html>
<html lang="en">
<head>
<meta charset="utf-8">
<title>Northridge Design + Build — Business Card</title>
<link rel="stylesheet" href="https://fonts.googleapis.com/css2?family=Archivo:wght@400;700;900&display=swap">
<style>
  :root {
    --ink: #111111;
    --accent: #8cc63f;
    --paper: #ffffff;
  }
  html, body {
    margin: 0;
    padding: 0;
    overflow: hidden;
    background: var(--paper);
  }
  .card {
    position: relative;
    width: 1200px;
    height: 686px;
    background: var(--paper);
    overflow: hidden;
    font-family: "Archivo", Arial, sans-serif;
    color: var(--ink);
  }
  .brand {
    position: absolute;
    left: 0;
    right: 0;
    top: 300px;
    display: flex;
    justify-content: center;
    align-items: center;
    gap: 22px;
  }
  .brand-square {
    width: 58px;
    height: 58px;
    background: var(--accent);
  }
  .brand-name {
    margin: 0;
    font-weight: 900;
    font-size: 78px;
    line-height: 1;
    letter-spacing: 2px;
    color: var(--ink);
  }
  .rule {
    position: absolute;
    left: 336px;
    width: 526px;
    top: 390px;
    height: 2px;
    background: var(--ink);
  }
  .tagline {
    position: absolute;
    left: 0;
    right: 0;
    top: 398px;
    margin: 0;
    text-align: center;
    font-weight: 400;
    font-size: 29px;
    letter-spacing: 9px;
    color: var(--ink);
  }
  .tagline .plus {
    font-weight: 900;
  }
  .website {
    position: absolute;
    left: 0;
    right: 0;
    top: 536px;
    margin: 0;
    text-align: center;
    font-weight: 700;
    font-size: 21px;
    letter-spacing: 4px;
    color: var(--ink);
  }
</style>
</head>
<body>
  <main class="card">
    <div class="brand">
      <span class="brand-square" aria-hidden="true"></span>
      <h1 class="brand-name">NORTHRIDGE</h1>
    </div>
    <div class="rule" aria-hidden="true"></div>
    <p class="tagline">DESIGN <span class="plus">+</span> BUILD</p>
    <p class="website">WWW.NORTHRIDGEBUILD.COM</p>
  </main>
</body>
</html>
```